【 概要 】 証券会社の比較サイトで使用するヘッドバナー(ヘッダーバナー)デザインを募集します。 比較サイトは広告出稿用のもので、サイトの最上部に置く予定のバナーです。 【 依頼内容 】 ■サイズ: 横750px × 縦350px ■作成数: 1種類 ■利用用途:リスティング広告の比較サイトの最上部バナー →ユーザーが広告をクリックし比較サイトに流入するときに、まず目に入るバナーになります。 【 デザインイメージ 】 ■ターゲット層:20~30代の投資初心者 ■雰囲気:安心感・信頼感・初心者向けであることの明確さ ■ベースカラー:緑色系(落ち着いたトーン) ■文字 「2026年最新版」「NISA初心者でも安心」「失敗しない ネット証券ランキング」の3つは必ず入れていただきたいです。 文字色やレイアウト、装飾はお任せします。全体の雰囲気に合わせてください。 必要に応じて文字を追加していただいて構いません。 ~優先度~ ① NISA初心者でも安心(最も大きく・目立たせる) ② 失敗しない ネット証券ランキング ③ 2026年最新版 ※一目で「初心者向けの比較ランキングサイト」と伝わる構成を希望します。 ■画像 その他、バナー作成時に必要な素材がある際はVELQOから引用し、カンプデータで作成してください。 ※採用時には素材番号を伺います。 ※人物写真は、可能であれば使用してください。 イラストではなく、リアルな人物写真を希望します。 【VELQO URL】 https://velqo.jp/ ■AIツールの使用について AIツールの使用は可 ■著作権・利用権について 納品物は、第三者の著作権・商標権等を侵害しないものに限ります。 使用素材・フォント・AI生成物等についても、 商用利用が可能なものをご使用ください。 【納品方法】 ・jpg、psdの2つとも納品お願いします。 【 契約金額(税抜) 】 15,000円 ※契約金額(税込)からシステム利用料を差し引いた金額が、ワーカーさまの受取金額となります。 その他ご質問等ありましたら、気軽にお問い合わせください。 ご応募をお待ちしております! |
視認性・デザイン性・インパクト・サイトとの親和性など、複数の観点から総合的に評価した結果、
今回の募集内容およびサイトの目的に最も適しているバナーであると判断し、採用させていただきました。
皆様、このたびはご応募いただき誠にありがとうございました。
100件を超えるご提案をお寄せいただき、いずれも魅力的な内容であったため、選定にあたり大変悩みました。
また機会がございましたら、ぜひよろしくお願いいたします。

```html
<!DOCTYPE html>
<html lang="ja">
<head>
<meta charset="UTF-8">
<title>NISA初心者でも安心 ネット証券ランキング</title>
<link rel="stylesheet" href="https://fonts.googleapis.com/css2?family=M+PLUS+Rounded+1c:wght@500;800&family=Montserrat:wght@300&family=Playfair+Display:wght@500&display=swap">
<style>
  :root {
    --bg: #f4f5f3;
    --mint: #c9ecd3;
    --mint-soft: #dff3e4;
    --yellow: #f7f1a6;
    --band: #1f6a37;
    --band-dark: #17532a;
    --green-text: #236b35;
    --ink: #3a3a3a;
    --white: #ffffff;
    --star: #f2d23c;
  }
  html, body { margin: 0; padding: 0; overflow: hidden; background: var(--bg); }
  .banner {
    position: relative;
    width: 1200px; height: 560px;
    overflow: hidden;
    background: linear-gradient(180deg, #fafbf9 0%, var(--bg) 100%);
    font-family: "M PLUS Rounded 1c", sans-serif;
  }
  .backdrop { position: absolute; inset: 0; }
  .model-photo {
    position: absolute; left: 0; top: 0;
    width: 440px; height: 560px;
    background:
      radial-gradient(ellipse at 45% 30%, #e9ddd2 0%, rgba(233,221,210,0) 45%),
      linear-gradient(180deg, #ece8e3 0%, #f1f0ee 55%, #dcdfdc 100%);
    -webkit-mask-image: linear-gradient(90deg, #000 75%, transparent 100%);
    mask-image: linear-gradient(90deg, #000 75%, transparent 100%);
  }
  .headline-en {
    position: absolute; left: 238px; top: 18px;
    margin: 0;
    font-family: "Montserrat", sans-serif; font-weight: 300;
    font-size: 232px; line-height: 1; letter-spacing: 14px;
    color: transparent;
    -webkit-text-stroke: 3px var(--ink);
  }
  .headline {
    position: absolute; left: 258px; top: 205px;
    margin: 0;
    font-weight: 800; font-size: 116px; line-height: 1;
    letter-spacing: 2px;
    color: var(--green-text);
  }
  .beginner-mark { position: absolute; left: 388px; top: 128px; width: 70px; height: 92px; }
  .edition {
    position: absolute; left: 982px; top: 40px;
    font-weight: 800; color: var(--ink);
    text-align: center; line-height: 1.1;
  }
  .edition .year { display: block; font-size: 44px; }
  .edition .label { display: block; font-size: 44px; }
  .rank-word {
    position: absolute; left: 280px; top: 490px;
    font-family: "Playfair Display", serif; font-weight: 500;
    font-size: 46px; letter-spacing: 8px;
    color: rgba(255,255,255,0.28);
  }
  .tagline { position: absolute; left: 560px; top: 420px; transform: rotate(-4deg); transform-origin: left top; }
  .tag {
    display: inline-block;
    background: var(--white);
    color: var(--green-text);
    font-weight: 500;
    padding: 4px 18px;
    line-height: 1.15;
    box-shadow: 0 3px 8px rgba(0,0,0,0.15);
  }
  .tag-lead { font-size: 50px; margin-left: 4px; }
  .tag-main { font-size: 54px; margin-top: 6px; letter-spacing: 2px; }
  .stars { position: absolute; left: 890px; top: 408px; width: 120px; height: 36px; transform: rotate(-4deg); }
</style>
</head>
<body>
<div class="banner">
  <svg class="backdrop" width="1200" height="560" viewBox="0 0 1200 560" aria-hidden="true">
    <circle cx="790" cy="60" r="130" fill="var(--mint)"/>
    <circle cx="1130" cy="110" r="175" fill="var(--yellow)"/>
    <circle cx="1110" cy="340" r="120" fill="var(--mint-soft)"/>
    <path d="M0,455 C320,420 760,380 1200,320 L1200,560 L0,560 Z" fill="var(--band)"/>
    <path d="M0,500 C380,470 820,430 1200,380 L1200,560 L0,560 Z" fill="var(--band-dark)" opacity="0.35"/>
  </svg>

  <div class="rank-word">RANKING</div>

  <div class="model-photo" role="img" aria-label="白いシャツを着た笑顔の女性の写真"></div>

  <h1 class="headline-en">NISA</h1>

  <svg class="beginner-mark" viewBox="0 0 70 92" aria-hidden="true">
    <path d="M35,20 L6,4 L6,62 L35,88 Z" fill="#f5d31a"/>
    <path d="M35,20 L64,4 L64,62 L35,88 Z" fill="#2e9a45"/>
  </svg>

  <h2 class="headline">初心者でも安心</h2>

  <div class="edition">
    <span class="year">2026年</span>
    <span class="label">最新版</span>
  </div>

  <svg class="stars" viewBox="0 0 120 36" aria-hidden="true">
    <g fill="var(--star)">
      <polygon points="18,2 22.5,12.5 34,13.5 25,21 28,33 18,26.5 8,33 11,21 2,13.5 13.5,12.5"/>
      <polygon points="60,2 64.5,12.5 76,13.5 67,21 70,33 60,26.5 50,33 53,21 44,13.5 55.5,12.5"/>
      <polygon points="102,2 106.5,12.5 118,13.5 109,21 112,33 102,26.5 92,33 95,21 86,13.5 97.5,12.5"/>
    </g>
  </svg>

  <div class="tagline">
    <div class="tag tag-lead">失敗しない</div><br>
    <div class="tag tag-main">ネット証券ランキング</div>
  </div>
</div>
</body>
</html>
```